Business card for Eyelash extension salon in Alderwyn Hills,California USA

We need new business card for our salon in Alderwyn Hills. The salon name is 'Lumarra' . We would like to have...Business name: Lumarra Name of person: will provide later Address 6128 N.Corbel Ridge Blvd Alderwyn Hills , CA 90999 Phone: will provide later (Text only) Web: www.lumarrastudio-example.com Pictogrid icon, Friendvale icon follow us for seasonal campaign and news @lumarrastudioexample Design should look elegant, high-end, clean, simple, cohesive with my brand. Please refer my brand board. Business name color will be metallic bronzy color. Im thinking grey background or white background. Thanks

Target Market(s)

25-35. Gender neutral. People who are in Entertainment business industry.
This is High-end Eyelash extension salon in Alderwyn Hills

Industry/Entity Type

Beauty Salon

Contact Information for Business Card

Business name: Lumarra
Name of person: will provide later
Address 6128 N.Corbel Ridge Blvd Alderwyn Hills , CA 90999
Phone: will provide later (Text only)
Web: www.lumarrastudio-example.com
Pictogrid icon, Friendvale icon
follow us for seasonal campaign and news @lumarrastudioexample

Requirements
Must have
• Beautiful, elegant, clean and simple look but very attractive and modern
Should not have
• We don't like too clutter, too busy designs.

```html
<!DOCTYPE html>
<html lang="en">
<head>
<meta charset="utf-8">
<title>Lumarra Business Card</title>
<link rel="stylesheet" href="https://fonts.googleapis.com/css2?family=Playfair+Display:wght@500&family=Poppins:wght@300;400;500&display=swap">
<style>
  :root {
    --backdrop: #2a2c30;
    --card: #ffffff;
    --bronze: #8f6a4e;
    --marble-light: #f3f3f4;
    --marble-mid: #dcdde0;
    --ink: #4f4f52;
    --on-bronze: #ffffff;
  }
  * { margin: 0; padding: 0; box-sizing: border-box; }
  html, body {
    width: 1200px; height: 900px; overflow: hidden;
    background: var(--backdrop);
    font-family: "Poppins", sans-serif;
  }
  .canvas { position: relative; width: 1200px; height: 900px; }

  .card {
    position: absolute;
    background: var(--card);
    border-radius: 24px;
    overflow: hidden;
    box-shadow: 0 14px 30px rgba(0,0,0,.35);
  }
  .marble {
    position: absolute;
    background:
      radial-gradient(ellipse at 30% 25%, var(--marble-mid) 0%, transparent 45%),
      radial-gradient(ellipse at 75% 70%, var(--marble-mid) 0%, transparent 40%),
      var(--marble-light);
  }

  /* Front */
  .card-front { left: 110px; top: 160px; width: 332px; height: 580px; }
  .card-front .marble { inset: 0 0 168px 0; }
  .brand {
    position: absolute; left: 0; right: 0; top: 150px;
    text-align: center;
  }
  .brand-name {
    font-family: "Poppins", sans-serif;
    font-weight: 300;
    font-size: 58px;
    letter-spacing: 2px;
    color: var(--bronze);
  }
  .brand-place {
    margin-top: 14px;
    font-size: 11px;
    letter-spacing: 4px;
    color: var(--bronze);
  }
  .address-band {
    position: absolute; left: 0; right: 0; bottom: 0; height: 168px;
    background: var(--bronze);
    color: var(--on-bronze);
    padding: 0 30px;
    display: flex; flex-direction: column; justify-content: center;
    font-size: 16px; line-height: 1.45;
    white-space: nowrap;
  }

  /* Back */
  .card-back { left: 500px; top: 270px; width: 590px; height: 338px; }
  .card-back .marble { left: 0; top: 20px; width: 320px; height: 262px; }
  .name-band {
    position: absolute; left: 0; top: 70px; width: 320px; height: 52px;
    background: var(--bronze);
    display: flex; align-items: center; padding-left: 34px;
    font-family: "Playfair Display", serif;
    font-weight: 500;
    font-size: 19px; letter-spacing: 1.5px;
    color: var(--on-bronze);
  }
  .contact {
    position: absolute; left: 346px; top: 52px; width: 232px;
    color: var(--ink);
    font-size: 14px;
    white-space: nowrap;
  }
  .follow { font-weight: 500; line-height: 1.35; }
  .social { display: flex; gap: 8px; margin: 28px 0 0 38px; }
  .social-dot { width: 22px; height: 22px; border-radius: 50%; background: var(--bronze); }
  .handle { margin-top: 6px; font-weight: 500; }
  .lines { margin-top: 38px; line-height: 1.4; font-size: 13.5px; }
</style>
</head>
<body>
<main class="canvas">
  <section class="card card-front" aria-label="Front of business card">
    <div class="marble" role="img" aria-label="White and grey marble texture"></div>
    <div class="brand">
      <div class="brand-name">Lumarra</div>
      <div class="brand-place">ALDERWYN HILLS</div>
    </div>
    <div class="address-band">
      <span>6128 N.Corbel Ridge Blvd</span>
      <span>Alderwyn Hills , CA 90999</span>
    </div>
  </section>

  <section class="card card-back" aria-label="Back of business card">
    <div class="marble" role="img" aria-label="White and grey marble texture"></div>
    <div class="name-band">JOHNATHAN DOE</div>
    <div class="contact">
      <p class="follow">Follow us for seasonal<br>campaign and news</p>
      <div class="social">
        <span class="social-dot" aria-label="Friendvale"></span>
        <span class="social-dot" aria-label="Pictogrid"></span>
      </div>
      <p class="handle">@lumarrastudioexample</p>
      <p class="lines">123 456 7890 (text only)<br>www.lumarrastudio-example.com</p>
    </div>
  </section>
</main>
</body>
</html>
```